BRELTONAllies.co.uk - Mental Health Clinic for Child and Adolescents

Updated 29/01/2018***
I am not sure you guys are getting the idea regards to the opening page / homescreen layout. Can you look at the new images I have uploaded (page 5, 6 and 7) These are some of the layouts I like but to incorporate my chosen images, with the BRELTON commissioner, buttons and a sliding header bar.
I have written a strong brief, I am looking for a website, preferably wordpress as i know they are easy to maintain. I am looking for a one page site, with the top / opening page being full screen image with drop down categories. I have made a rough design, see full brief in word doc attached, there is some freedom to play around with the design aspect but it will need to relay all the content provided. I like a minimal feel. I have also attached some images that may be useful, but will need a new logo for BRELTON Allies. I have attached some logo idea's, it is up to you decide whether you want to use them.
I would prefer the homepage as full screen image, and the categories offered as a drop down or over the main image.
I have also attached linked to some competitors websites:
https://www.vorrendale-group.co.uk/
http://www.qmvd.org.uk/
Industry/Entity Type
Clinic
Number of Pages Required
1 page
Font styles to use
Look and feel
Each slider illustrates characteristics of the customer's brand and the style your logo design should communicate.

```html
<!DOCTYPE html>
<html lang="en">
<head>
<meta charset="utf-8">
<title>BRELTON Allies</title>
<link rel="stylesheet" href="https://fonts.googleapis.com/css2?family=Open+Sans:wght@400;600&family=Roboto+Condensed:wght@400;700&display=swap">
<style>
:root{
  --ink:#222;
  --body:#555;
  --cream:#fdfcf2;
  --yellow:#f2e400;
  --teal:#1ab3c9;
  --magenta:#e6137f;
  --lime:#9bc424;
  --blue:#1565a8;
  --green:#0a9c86;
  --footer:#1b1b1b;
  --white:#fff;
}
*{box-sizing:border-box;margin:0;padding:0}
html,body{width:828px;height:1200px;overflow:hidden;background:var(--white)}
body{position:relative;font-family:"Open Sans",sans-serif;color:var(--ink)}
.abs{position:absolute}

/* hero */
.hero{position:absolute;left:0;top:0;width:828px;height:394px;overflow:hidden}
.hero-photo{position:absolute;inset:0;background:linear-gradient(120deg,#8c8478 0%,#b9b2a6 40%,#d8d3cb 70%,#9a8a74 100%)}
.hero-shade{position:absolute;inset:0;background:rgba(0,0,0,.18)}
.sidebar{position:absolute;left:0;top:0;width:216px;height:394px}
.brand{position:absolute;left:58px;top:38px;display:flex;align-items:center;gap:6px;font-family:"Roboto Condensed",sans-serif;font-weight:700;font-size:20px;color:var(--magenta)}
.brand-dot{width:18px;height:18px;border-radius:50%;background:var(--yellow)}
.nav{position:absolute;left:0;top:104px;width:204px;list-style:none;text-align:center;font-size:12px}
.nav li{height:26.6px;line-height:26.6px;color:var(--ink)}
.nav li.active{color:var(--teal)}
.hero-title{position:absolute;left:330px;width:368px;top:178px;text-align:center;font-family:"Roboto Condensed",sans-serif;font-weight:700;font-size:34px;color:var(--white);letter-spacing:.3px}
.pill{position:absolute;top:234px;height:32px;border-radius:16px;color:var(--white);font-size:13px;display:flex;align-items:center;justify-content:center}
.pill-parents{left:379px;width:123px;background:var(--teal)}
.pill-commissioners{left:510px;width:139px;background:var(--magenta);border:2px solid #f24a9e}
.slider-dots{position:absolute;left:795px;top:191px;display:flex;flex-direction:column;gap:5px}
.slider-dots span{width:6px;height:6px;border-radius:50%;background:var(--white)}
.slider-dots span:first-child{background:var(--lime)}
.caption-bar{position:absolute;left:180px;top:350px;width:648px;height:44px;background:rgba(40,40,40,.75);display:flex;align-items:center;justify-content:center;color:var(--white);font-size:17px}
.caption-bar svg{position:absolute;top:14px}

/* welcome */
.welcome-title{position:absolute;left:63px;top:472px;font-family:"Roboto Condensed",sans-serif;font-size:23px;font-weight:400;color:var(--ink)}
.welcome-text{position:absolute;left:63px;top:505px;width:371px;font-size:9.6px;line-height:16.8px;color:var(--body);text-align:justify}
.btn-more{position:absolute;left:62px;top:617px;width:76px;height:22px;border-radius:11px;background:var(--lime);color:var(--white);font-size:8.5px;font-weight:600;display:flex;align-items:center;justify-content:center}
.video{position:absolute;left:466px;top:457px;width:297px;height:188px;border:2px solid var(--white);box-shadow:0 3px 10px rgba(0,0,0,.18);background:linear-gradient(180deg,#e9e9e7 0%,#c9c7c1 55%,#5e7f7c 100%)}
.video svg{position:absolute;left:126px;top:72px}

/* contact */
.contact{position:absolute;left:0;top:702px;width:828px;height:342px;background:linear-gradient(100deg,var(--blue) 0%,#117c9e 50%,var(--green) 100%);color:var(--white)}
.contact-title{position:absolute;left:0;width:828px;top:40px;text-align:center;font-family:"Roboto Condensed",sans-serif;font-weight:700;font-size:28px}
.contact-sub{position:absolute;left:0;width:828px;top:76px;text-align:center;font-size:11px}
.field{position:absolute;left:128px;width:236px;height:30px;background:var(--white);color:#555;font-size:10px;padding:8px 11px}
.field-message{height:44px}
.btn-submit{position:absolute;left:128px;top:274px;width:81px;height:23px;border-radius:12px;background:var(--lime);color:var(--white);font-size:11px;display:flex;align-items:center;justify-content:center}
.info{position:absolute;left:398px;display:flex;gap:11px;font-size:11px;line-height:14.5px}
.info svg{flex:none;margin-top:4px}

/* footer */
.footer{position:absolute;left:0;top:1044px;width:828px;height:156px;background:var(--footer);color:var(--white)}
.footer-brand{position:absolute;left:0;width:828px;top:33px;display:flex;justify-content:center;align-items:center;gap:8px;font-family:"Roboto Condensed",sans-serif;font-weight:700;font-size:22px;color:var(--yellow)}
.footer-brand .brand-dot{width:24px;height:24px}
.social{position:absolute;left:0;width:828px;top:93px;display:flex;justify-content:center;gap:6px}
.social span{width:24px;height:24px;border-radius:50%;border:1.5px solid var(--white)}
.copyright{position:absolute;left:0;width:828px;top:125px;text-align:center;font-size:9.6px}
</style>
</head>
<body>

<section class="hero">
  <div class="hero-photo" role="img" aria-label="Photo of a therapist with notes talking with a young boy in a bright room"></div>
  <div class="hero-shade"></div>
  <svg class="sidebar" width="216" height="394" viewBox="0 0 216 394">
    <polygon points="0,0 216,0 176,394 0,394" fill="#1a1a1a" opacity=".15" transform="translate(2,2)"/>
    <polygon points="208,0 216,0 178,394 170,394" fill="var(--yellow)"/>
    <polygon points="0,0 208,0 170,394 0,394" fill="var(--cream)"/>
  </svg>
  <div class="brand"><span class="brand-dot"></span>BRELTON</div>
  <ul class="nav">
    <li class="active">Home</li>
    <li>About us</li>
    <li>Our Team</li>
    <li>Our Services</li>
    <li>Contact us</li>
    <li>Parents</li>
    <li>Commissioners</li>
    <li>Blog</li>
    <li>Forum</li>
  </ul>
  <h1 class="hero-title">BRELTON ALLIES</h1>
  <div class="pill pill-parents">PARENTS</div>
  <div class="pill pill-commissioners">COMMISSIONERS</div>
  <div class="slider-dots"><span></span><span></span><span></span><span></span><span></span></div>
  <div class="caption-bar">
    <svg style="left:30px" width="10" height="16" viewBox="0 0 10 16"><path d="M8 2 2 8l6 6" fill="none" stroke="#fff" stroke-width="2"/></svg>
    ADHD and autism screening within 24 hours
    <svg style="left:578px" width="10" height="16" viewBox="0 0 10 16"><path d="M2 2l6 6-6 6" fill="none" stroke="#fff" stroke-width="2"/></svg>
  </div>
</section>

<h2 class="welcome-title">WELCOME TO BRELTON ALLIES</h2>
<p class="welcome-text">It is a long established fact that a reader will be distracted by the readable content of a page when looking at its layout. The point of using Lorem Ipsum is that it has a more-or-less normal distribution of letters, as opposed to using 'Content here, content here', making it look like readable English. Many desktop publishing packages and web page editors now use Lorem Ipsum as their default model text, and a search for 'lorem ipsum' will uncover many web sites still in their infancy</p>
<div class="btn-more">Read More »</div>
<div class="video" role="img" aria-label="Video still of five smiling teenagers sitting together on a sofa">
  <svg width="42" height="42" viewBox="0 0 42 42"><circle cx="21" cy="21" r="20" fill="rgba(0,0,0,.45)"/><path d="M16 12l13 9-13 9z" fill="#fff"/></svg>
</div>

<section class="contact">
  <h2 class="contact-title">CONTACT US</h2>
  <p class="contact-sub">Neque porro quisquam est qui dolorem ipsum quia dolor sit amet</p>
  <div class="field" style="top:120px">Name</div>
  <div class="field" style="top:154px">Phone number</div>
  <div class="field" style="top:188px">Email address</div>
  <div class="field field-message" style="top:222px">Message</div>
  <div class="btn-submit">Submit</div>

  <div class="info" style="top:126px">
    <svg width="12" height="12" viewBox="0 0 24 24"><path d="M6.6 10.8a15 15 0 0 0 6.6 6.6l2.2-2.2c.3-.3.7-.4 1-.2 1.1.4 2.3.6 3.6.6.6 0 1 .4 1 1V20c0 .6-.4 1-1 1A17 17 0 0 1 3 4c0-.6.4-1 1-1h3.5c.6 0 1 .4 1 1 0 1.3.2 2.5.6 3.6.1.3 0 .7-.2 1z" fill="#fff"/></svg>
    <div>Phone Number :<br>0207 946 0321</div>
  </div>
  <div class="info" style="top:164px">
    <svg width="12" height="14" viewBox="0 0 24 28"><path d="M12 1a9 9 0 0 0-9 9c0 7 9 17 9 17s9-10 9-17a9 9 0 0 0-9-9zm0 12.5a3.5 3.5 0 1 1 0-7 3.5 3.5 0 0 1 0 7z" fill="#fff"/></svg>
    <div>Address :<br>Larkfield Suite 4B, 12-18 Mill Lane, London, E19 4TX</div>
  </div>
  <div class="info" style="top:196px">
    <svg width="12" height="12" viewBox="0 0 24 24"><circle cx="12" cy="12" r="10" fill="none" stroke="#fff" stroke-width="2.5"/><path d="M12 6v6l-4 2" fill="none" stroke="#fff" stroke-width="2.5"/></svg>
    <div>Opening Times:<br>9am – 5pm Mon-Fri</div>
  </div>
  <div class="info" style="top:234px">
    <svg width="13" height="11" viewBox="0 0 26 20"><path d="M1 3l12 8 12-8V1H1z M1 6v13h24V6l-12 8z" fill="#fff"/></svg>
    <div>Email:<br>enquiry@breltonallies.co.uk</div>
  </div>
</section>

<footer class="footer">
  <div class="footer-brand"><span class="brand-dot"></span>BRELTON</div>
  <div class="social"><span></span><span></span><span></span><span></span><span></span><span></span></div>
  <p class="copyright">Copyright © 2018&nbsp; All Rights Reserved</p>
</footer>

</body>
</html>
```